Amber Hollow Gathering - Promotional Poster

Amber Hollow Gathering is a party by the people, for the people. It’s where the grooviest group of creatives comes together to dream, connect, learn and inspire. This incredible forest-stomping celebration is returning in 2023 with our latest event “Velvet Jamboree”
We need your help to create consistent branding that will make the event memorable and recognisable to our attendees. To start with we need a poster announcing the festival theme and our artists for this year.
Here are the key elements we would like you to include in your design:
1. Theme: The branding should reflect the theme of "Velvet Jamboree" with vibrant colours, cosmic imagery, carnival imagery, and celestial elements. It should evoke a sense of wonder, excitement, and adventure.
2. Logo - It should include our Amber Hollow Logo. AI file attached.
3. Text - Amber Hollow (or logo) Presents Velvet Jamboree”
Must haves -
- The logo or festival name
- The Date 5-8th May 2023
- Location - Mudgee NSW
- ticket link www.amberhollowgathering.com
- artist names put in alphabetical order.
Marta Quillby
Pieter Renwold
Fig moss
Tobias Wrenfield
Murfolk
Rosie K
Nora F
Dominic Pryle
Ivo marrantes
Greta Vane
Hana P
Perdu
Vim Ostra
Otis R & Quen
4. Colour scheme: The colour scheme should be consistent with the theme of "Velvet Jamboree." We would like a range of bold and bright colours that reflect the colours of the cosmos such as purple, blue, and pink.
5. Typography: The typography should be clear and easy to read. We would like a font that reflects the Velvet Jamboree theme.
6. Graphical elements - The poster may include pictorial elements, stars, planets, moons, galaxies, carnival imagery.
7. Marketing collateral: For the winner of this project we need marketing collateral that is consistent with the branding, including artist tiles, posters, banners, social media graphics, and other promotional materials.
8. Deliverables - We need the .Ai .Id or photoshop files at the end of this project.
You can view videos & details of our past events at www.amberhollowgathering.com or on instagram.com/amber_hollow_gathering
We are excited to see your ideas and look forward to working with you

```html
<!DOCTYPE html>
<html lang="en">
<head>
<meta charset="utf-8">
<title>Amber Hollow Gathering presents Velvet Jamboree 2023</title>
<link rel="stylesheet" href="https://fonts.googleapis.com/css2?family=Questrial&family=Yellowtail&family=Dancing+Script:wght@500&display=block">
<style>
  :root {
    --night: #0d0c33;
    --night-deep: #07072a;
    --magenta: #b3268f;
    --rose: #e0528a;
    --amber: #f0a54a;
    --violet: #5b2a8c;
    --sky-blue: #1b8fd6;
    --tree-blue: #2a7fb3;
    --gold: #f2c766;
    --link-gold: #e9bf45;
    --white: #ffffff;
    --disc: #1b1a36;
  }
  * { margin: 0; padding: 0; box-sizing: border-box; }
  html, body { width: 847px; height: 1200px; overflow: hidden; background: var(--night-deep); }
  .poster {
    position: relative;
    width: 847px;
    height: 1200px;
    overflow: hidden;
    font-family: "Questrial", "Century Gothic", sans-serif;
    color: var(--white);
    background:
      radial-gradient(ellipse 520px 260px at 50% 760px, rgba(179,38,143,0.85), rgba(179,38,143,0) 70%),
      linear-gradient(180deg, var(--violet) 0%, var(--magenta) 55%, #3a1460 70%, var(--night) 80%, var(--night-deep) 100%);
  }
  .event-photography {
    position: absolute;
    left: 0; top: 0;
    width: 847px; height: 600px;
    background:
      radial-gradient(circle 160px at 680px 170px, rgba(240,165,74,0.8), rgba(240,165,74,0) 75%),
      radial-gradient(circle 200px at 120px 200px, rgba(120,80,170,0.75), rgba(120,80,170,0) 75%),
      radial-gradient(circle 220px at 760px 420px, rgba(224,82,138,0.8), rgba(224,82,138,0) 75%),
      radial-gradient(circle 180px at 90px 470px, rgba(214,112,160,0.7), rgba(214,112,160,0) 75%),
      linear-gradient(180deg, #3a2c6e 0%, #7a3f8c 40%, #c0528a 80%, rgba(192,82,138,0) 100%);
  }
  .tree-silhouette {
    position: absolute;
    top: 560px;
    width: 330px; height: 520px;
  }
  .tree-silhouette--left {
    left: 0;
    background: radial-gradient(ellipse 220px 260px at 60px 160px, rgba(42,127,179,0.85), rgba(42,127,179,0) 75%);
  }
  .tree-silhouette--right {
    right: 0;
    background: radial-gradient(ellipse 220px 260px at 270px 180px, rgba(42,127,179,0.85), rgba(42,127,179,0) 75%);
  }
  .title-disc {
    position: absolute;
    left: 155px; top: 212px;
    width: 536px; height: 536px;
    border-radius: 50%;
    border: 6px solid var(--sky-blue);
    background: radial-gradient(circle at 45% 40%, #2a2848 0%, var(--disc) 55%, #121128 100%);
  }
  .brand-name {
    position: absolute;
    left: 0; width: 847px; top: 308px;
    text-align: center;
    font-size: 20px;
    letter-spacing: 6px;
    line-height: 1.3;
    color: var(--white);
  }
  .brand-name span { display: block; font-size: 11px; letter-spacing: 7px; }
  .presents {
    position: absolute;
    left: 0; width: 847px; top: 350px;
    text-align: center;
    font-family: "Yellowtail", "Dancing Script", cursive;
    font-size: 34px;
    line-height: 1.2;
    color: var(--white);
  }
  .event-title {
    position: absolute;
    left: 123px; top: 410px;
    width: 600px;
    text-align: center;
    font-family: "Yellowtail", "Dancing Script", cursive;
    color: var(--gold);
    transform: rotate(-12deg);
    line-height: 0.95;
    font-weight: 400;
  }
  .event-title__name { display: block; font-size: 74px; white-space: nowrap; }
  .event-title__year { display: block; font-size: 70px; margin-left: -40px; }
  .event-details {
    position: absolute;
    left: 0; width: 847px; top: 624px;
    text-align: center;
    font-size: 28px;
    line-height: 38px;
    color: var(--white);
  }
  .artists-heading {
    position: absolute;
    left: 0; width: 847px; top: 768px;
    text-align: center;
    font-family: "Yellowtail", "Dancing Script", cursive;
    font-size: 54px;
    line-height: 1.1;
    color: var(--gold);
    font-weight: 400;
  }
  .artist-list {
    position: absolute;
    top: 846px;
    list-style: none;
    font-size: 20px;
    line-height: 37.3px;
  }
  .artist-list--first { left: 273px; }
  .artist-list--second { left: 457px; }
  .ticket-line {
    position: absolute;
    left: 0; width: 847px; top: 1129px;
    text-align: center;
    font-size: 22px;
    color: var(--white);
  }
  .ticket-line a { color: var(--link-gold); text-decoration: none; }
</style>
</head>
<body>
<main class="poster">
  <div class="event-photography" role="img" aria-label="Festival photography of costumed performers with a glowing light hoop, washed in pink, orange and purple light"></div>
  <div class="tree-silhouette tree-silhouette--left" role="img" aria-label="Blue tree silhouette"></div>
  <div class="tree-silhouette tree-silhouette--right" role="img" aria-label="Blue tree silhouette"></div>

  <div class="title-disc"></div>

  <p class="brand-name">AMBER HOLLOW<span>GATHERING</span></p>
  <p class="presents">presents</p>

  <h1 class="event-title">
    <span class="event-title__name">Velvet Jamboree</span>
    <span class="event-title__year">2023</span>
  </h1>

  <p class="event-details">5th - 8th May 2023<br>Mudgee, NSW</p>

  <h2 class="artists-heading">Artists</h2>
  <ul class="artist-list artist-list--first">
    <li>Dominic Pryle</li>
    <li>Fig Moss</li>
    <li>Greta Vane</li>
    <li>Hana P</li>
    <li>Ivo Marrantes</li>
    <li>Marta Quillby</li>
    <li>Murfolk</li>
  </ul>
  <ul class="artist-list artist-list--second">
    <li>Nora F</li>
    <li>Otis R &amp; Quen</li>
    <li>Perdu</li>
    <li>Pieter Renwold</li>
    <li>Rosie K</li>
    <li>Tobias Wrenfield</li>
    <li>Vim Ostra</li>
  </ul>

  <p class="ticket-line">For tickets, visit: <a href="#">www.amberhollowgathering.com</a></p>
</main>
</body>
</html>
```